Gretls SohlenGlück Fußpflegestudio Neueröffnungs-Flyer & Gutschein – A4-Flyer-D...

Projektbeschreibung:
Wir benötigen ein ansprechendes A4-Flyer-Design für die Neueröffnung von "Gretls SohlenGlück", einem professionellen Fußpflege-Studio in Bad Radkersburg. Der Flyer soll das Studio und seine Leistungen vorstellen und einen exklusiven Eröffnungsgutschein enthalten. Der Gutschein befindet sich im unteren Bereich des Flyers und muss durch eine deutlich sichtbare Schnittlinie abtrennbar gestaltet werden, sodass Kunden ihn einfach herausschneiden können. Zusätzlich wird ein passendes Logo für "Gretls SohlenGlück" benötigt.

Designanforderungen:
Flyer Format: A4, Hochformat.

Sprache:
Deutsch

Struktur:
Flyer-Text im oberen Bereich, Gutscheinbereich im unteren Drittel.

Schnittlinie: Gestalten Sie eine deutlich sichtbare, gestrichelte Linie zwischen dem Flyertext und dem Gutscheinbereich mit einer kleinen Scherensymbol-Darstellung am Rand, um klar zu zeigen, dass dieser Bereich abgeschnitten werden kann.

Gestaltungsstil:
Einladend, professionell und passend zu einem Fußpflege-Studio. Die Farben sollten sanft und beruhigend wirken: vorwiegend Türkis und Weiß, eventuell kombiniert mit Rosa.

Textgestaltung:
Die folgenden Texte müssen in den jeweiligen Bereichen des Flyers und des Gutscheins integriert und klar strukturiert dargestellt werden:

Flyer Text:
Gretls SohlenGlück lädt Sie herzlich zur Neueröffnung ein!
Ihr neues Fußpflege-Studio in Bad Radkersburg.

Liebe Kundinnen und Kunden,
es ist endlich soweit: Mit viel Liebe und Leidenschaft öffnen wir die Türen zu unserem brandneuen Gretls SohlenGlück in der Lindacherweg 14, 8490 Bad Radkersburg!
Tauchen Sie ein in eine Welt, in der Ihre Füße verwöhnt und verschönert werden – ein Ort, an dem Entspannung und Pflege Hand in Hand gehen. Egal, ob Sie intensive Regeneration oder einen frischen Look für Ihre Füße wünschen – bei uns stehen Sie im Mittelpunkt!

Warum zu uns?
Bei Gretls SohlenGlück erwarten Sie wohltuende Behandlungen, die Sie nicht nur äußerlich strahlen lassen, sondern Ihnen auch ein tiefes Wohlgefühl schenken.
Wir gehen individuell auf Ihre Bedürfnisse ein und gestalten jeden Besuch zu einem besonderen Erlebnis, das Ihnen ein Lächeln ins Gesicht zaubert.

Terminvereinbarung
Unser Studio arbeitet mit einem Terminbetrieb, um Ihnen die bestmögliche Betreuung zu gewährleisten. Termine sind ausschließlich nach Vereinbarung möglich.
Ich freue mich sehr darauf, Ihre Reservierungen ab dem 15.10.2024 telefonisch unter 0664/29184637 entgegenzunehmen. Rufen Sie uns an und sichern Sie sich Ihren Wunschtermin!
Besuchen Sie uns in unserem gemütlichen und barrierefreien Ambiente und lassen Sie sich von unserer Expertise begeistern. Ihre Füße werden es Ihnen danken!
Ich freue mich schon sehr darauf, Sie persönlich bei Gretls SohlenGlück begrüßen zu dürfen!
Herzlichst, Ihre Milena Tavčar

Gutschein Text:
Exklusiver Eröffnungsgutschein*
Zur Feier unserer Neueröffnung möchten wir Ihnen etwas Besonderes schenken:
Profitieren Sie von 30 % Rabatt auf alle unsere Behandlungen – ein Geschenk für Sie und Ihre Füße!
*Dieser Gutschein ist gültig bis zum 31.12.2024 und einmalig einlösbar. Bitte beachten Sie, dass er nicht mit anderen Aktionen kombinierbar ist.

Gutscheinbereich: Der Gutschein soll optisch hervorstechen, z.B. durch Farbunterschiede, Rahmen oder Symbole. Der Text „Exklusiver Eröffnungsgutschein“ muss deutlich sichtbar sein und das Design soll den Eindruck eines wertvollen, einmaligen Angebots vermitteln.

Logo & Branding:
Das Logo soll passend zu einem Fußpflege-Studio gestaltet werden und sanfte, beruhigende Farben wie Türkis, Weiß und Rosa integrieren. Es sollte eine Mischung aus Schriftzug („Gretls SohlenGlück“) und einem passenden Symbol oder grafischem Element enthalten, das die Thematik der Fußpflege widerspiegelt.

Bilder & Elemente:
Optional können dezente Fußpflege-Bilder, Symbole (z.B. entspannende Füße, usw.) und weitere Elemente integriert werden, um das Design visuell zu unterstützen.

Ziel:
Der Flyer soll Kunden auf die Neueröffnung aufmerksam machen, Vertrauen aufbauen und den Gutschein als attraktives Angebot hervorheben. Die deutlich sichtbare Schnittlinie sorgt dafür, dass der Gutscheinbereich leicht abgetrennt und aufbewahrt werden kann.

```html
<!DOCTYPE html>
<html lang="de">
<head>
<meta charset="utf-8">
<title>Gretls SohlenGlück – Neueröffnung</title>
<link href="https://fonts.googleapis.com/css2?family=Playfair+Display:wght@600;700;800&family=Great+Vibes&family=Poppins:ital,wght@0,400;0,500;0,600;0,700;1,400&family=Oswald:wght@500;600&family=Bebas+Neue&display=swap" rel="stylesheet">
<style>
:root{
  --stage:#b9b9b9;
  --paper:#ffffff;
  --teal:#2bd6d0;
  --teal-text:#17a6a0;
  --pink:#f7a3d7;
  --pink-strong:#f062b9;
  --gold-a:#f8e866;
  --gold-b:#e2b53a;
  --gold-line:#d9a62c;
  --ink:#1d1d1f;
  --ink-soft:#333;
}
*{margin:0;padding:0;box-sizing:border-box}
html,body{width:907px;height:1200px;overflow:hidden;background:var(--stage)}
.flyer{position:absolute;left:71px;top:59px;width:766px;height:1083px;background:var(--paper);overflow:hidden;box-shadow:0 6px 14px rgba(0,0,0,.35)}
.hero-bg{position:absolute;left:0;top:0;width:766px;height:500px;background:linear-gradient(100deg,#ffffff 0%,#f0fbfc 45%,#d9f5f6 100%)}
.portrait{position:absolute;left:440px;top:30px;width:326px;height:450px;background:radial-gradient(ellipse 55% 50% at 55% 38%,#e8c9a8 0%,#d7a66a 40%,rgba(242,214,227,.9) 75%,rgba(246,221,233,0) 100%)}
.waves{position:absolute;left:0;top:0;width:766px;height:560px}
.brand-dot{position:absolute;left:112px;top:58px;width:28px;height:28px;border-radius:50%;background:var(--teal)}
.brand{position:absolute;left:49px;top:96px;font-family:"Playfair Display",serif;font-weight:700;font-size:34px;line-height:1.05;color:var(--pink)}
.headline{position:absolute;left:49px;top:203px;font-family:"Playfair Display",serif;font-weight:800;line-height:1}
.headline .l1{display:block;color:var(--pink);font-size:34px}
.headline .l2{display:block;color:var(--ink-soft);font-size:36px;margin-top:1px}
.headline .script{position:absolute;left:-7px;top:70px;font-family:"Great Vibes",cursive;font-weight:400;font-size:62px;color:var(--teal);white-space:nowrap}
.headline .ein{position:absolute;left:214px;top:110px;font-size:56px;color:#111;white-space:nowrap}
.subline{position:absolute;left:52px;top:370px;font-family:"Playfair Display",serif;font-size:15px;line-height:20px;color:var(--ink);font-weight:600;letter-spacing:.2px}
.subline b{font-weight:800}
.letter{position:absolute;left:50px;top:502px;width:507px;height:191px;background:var(--teal);border-radius:10px;padding:44px 14px 0 14px;font-family:"Poppins",sans-serif;color:var(--ink)}
.letter-tab{position:absolute;left:0;top:0;width:306px;height:36px;border-radius:10px 0 28px 0;background:linear-gradient(90deg,var(--gold-a),var(--gold-b));font-family:"Playfair Display",serif;font-weight:800;font-size:15px;line-height:38px;padding-left:13px}
.letter p{font-size:11.9px;line-height:14px}
.letter .address{font-weight:700;font-size:14.5px;line-height:20px;margin:1px 0 2px}
.letter .sign{font-weight:600;font-size:12px;margin-top:8px}
.bow{position:absolute;left:440px;top:470px;width:150px;height:130px;border-radius:40%;background:radial-gradient(ellipse,rgba(240,196,80,.75) 0%,rgba(240,196,80,0) 70%)}
.photo{position:absolute;width:122px;height:122px;border-radius:50%;border:5px solid var(--pink);box-shadow:0 0 0 3px #fff inset}
.photo-bath{left:585px;top:454px;background:radial-gradient(circle at 50% 60%,#a8644a,#d9b38f 80%)}
.photo-care{left:585px;top:581px;background:radial-gradient(circle at 50% 50%,#2f6fd8,#e6c2a8 75%)}
.booking-title{position:absolute;left:53px;top:718px;font-family:"Playfair Display",serif;font-weight:800;font-size:15px;color:var(--teal-text);letter-spacing:.3px}
.booking-lead{position:absolute;left:52px;top:751px;width:690px;font-family:"Poppins",sans-serif;font-weight:600;font-size:14.4px;line-height:19px;color:var(--ink)}
.booking-line{position:absolute;left:52px;font-family:"Poppins",sans-serif;font-size:17px;color:var(--ink)}
.booking-line.one{top:797px}
.booking-line.two{top:823px}
.date{position:absolute;left:571px;top:796px;width:135px;height:27px;background:var(--teal);border-radius:3px;font-family:"Poppins",sans-serif;font-weight:700;font-size:21px;line-height:28px;text-align:center;color:var(--ink)}
.phone{position:absolute;left:215px;top:826px;width:202px;height:23px;border:1px solid #f6b3d5;border-radius:4px;font-family:"Poppins",sans-serif;font-weight:700;font-size:20px;line-height:24px;color:var(--ink);padding-left:27px;white-space:nowrap}
.phone svg{position:absolute;left:2px;top:2px}
.phone-end{position:absolute;left:431px;top:823px;font-family:"Poppins",sans-serif;font-style:italic;font-size:17px;color:var(--ink)}
.cta{position:absolute;left:52px;top:860px;width:652px;height:28px;background:var(--pink-strong);border-radius:3px;font-family:"Playfair Display",serif;font-weight:600;font-size:15px;line-height:28px;letter-spacing:1.6px;color:#fff;text-align:center;white-space:nowrap}
.cut-line{position:absolute;left:0;top:916px;width:766px;border-top:1.5px dashed #333}
.voucher{position:absolute;left:0;top:918px;width:766px;height:165px;background:linear-gradient(100deg,#2ee0d8,#14d6e0 50%,#2bcbc4)}
.voucher-gold{position:absolute;left:0;top:0;width:279px;height:165px;background:linear-gradient(90deg,var(--gold-a),var(--gold-b))}
.v-title{position:absolute;left:40px;top:10px;width:210px;text-align:center;font-family:"Great Vibes",cursive;font-size:50px;color:#111;line-height:1.1;text-shadow:0 0 .6px #111}
.v-sub{position:absolute;left:51px;top:64px;width:197px;text-align:center;font-family:"Oswald",sans-serif;font-weight:600;font-size:20px;line-height:28px;color:#111;white-space:nowrap}
.v-note{position:absolute;left:56px;top:96px;width:186px;text-align:center;font-family:"Poppins",sans-serif;font-size:7.6px;line-height:9.5px;color:#222}
.v-bow{position:absolute;left:252px;top:14px;width:76px;height:114px;border-radius:40%;background:radial-gradient(ellipse,#f2c44c 0%,rgba(242,196,76,0) 72%)}
.v-kicker{position:absolute;left:342px;top:15px;font-family:"Poppins",sans-serif;font-weight:700;font-size:14px;letter-spacing:3.6px;color:#111;white-space:nowrap}
.v-percent{position:absolute;left:340px;top:28px;font-family:"Bebas Neue",sans-serif;font-size:74px;line-height:74px;color:#fff;white-space:nowrap}
.v-rabatt{position:absolute;left:455px;top:26px;font-family:"Playfair Display",serif;font-weight:800;font-size:26px;line-height:30px;color:#fff;white-space:nowrap}
.v-scope{position:absolute;left:456px;top:59px;font-family:"Poppins",sans-serif;font-weight:700;font-size:10.5px;line-height:14px;color:#111;white-space:nowrap}
.v-gift{position:absolute;left:574px;top:17px;width:126px;height:72px;border:1px solid #111;padding:8px 0 0 12px;font-family:"Poppins",sans-serif;font-weight:600;font-size:13.5px;line-height:18px;color:#111;white-space:nowrap}
.v-gift b{font-weight:700}
.v-terms{position:absolute;left:345px;top:99px;font-family:"Poppins",sans-serif;font-size:9.2px;line-height:12px;color:#111;white-space:nowrap}
</style>
</head>
<body>
<main class="flyer">
  <div class="hero-bg"></div>
  <div class="portrait" role="img" aria-label="Porträtfoto der Inhaberin im rosa Poloshirt"></div>
  <svg class="waves" viewBox="0 0 766 560" aria-hidden="true">
    <path d="M0 444 C150 449 280 494 390 488 C480 482 560 394 634 390 C690 387 740 424 766 455 L766 560 L0 560 Z" fill="#fff"/>
    <path d="M0 426 C150 426 300 468 420 462" fill="none" stroke="var(--gold-line)" stroke-width="6"/>
    <path d="M0 440 C150 445 280 490 390 484 C480 478 560 390 634 386 C690 383 740 420 766 451" fill="none" stroke="var(--pink)" stroke-width="9"/>
  </svg>

  <div class="brand-dot"></div>
  <div class="brand">Gretls<br>SohlenGlück</div>

  <h1 class="headline">
    <span class="l1">LÄDT SIE</span>
    <span class="l2">HERZLICH ZUR</span>
    <span class="script">Neueröffnung</span>
    <span class="ein">EIN!</span>
  </h1>
  <p class="subline"><b>IHR NEUES FUẞPFLEGE- UND<br>KOSMETIKSTUDIO</b> IN BAD RADKERSBURG.</p>

  <section class="letter">
    <div class="letter-tab">LIEBE KUNDINNEN UND KUNDEN,</div>
    <p>Es ist endlich soweit: Mit viel Liebe und Leidenschaft öffnen wir die Türen zu unserem brandneuen Gretls SohlenGlück in der</p>
    <p class="address">Lindacherweg 14, 8490 Bad Radkersburg!</p>
    <p>Besuchen Sie uns in unserem gemütlichen und barrierefreien Ambiente und lassen Sie sich von unserer Expertise begeistern. Ihre Füße werden es Ihnen danken! Ich freue mich schon sehr darauf, Sie persönlich bei Gretls SohlenGlück begrüßen zu dürfen!</p>
    <p class="sign">Herzlichst, Ihre Milena Tavčar</p>
  </section>
  <div class="bow" role="img" aria-label="Goldene Schleife"></div>

  <div class="photo photo-bath" role="img" aria-label="Foto: Füße im Blütenbad"></div>
  <div class="photo photo-care" role="img" aria-label="Foto: professionelle Fußpflege mit Handschuhen"></div>

  <h2 class="booking-title">TERMINVEREINBARUNG</h2>
  <p class="booking-lead">Unser Studio arbeitet mit einem Terminbetrieb, um Ihnen die bestmögliche Betreuung zu gewährleisten. Termine sind ausschließlich nach Vereinbarung möglich.</p>
  <p class="booking-line one">Ich freue mich sehr darauf, Ihre Reservierungen ab dem</p>
  <div class="date">15.10.2024</div>
  <p class="booking-line two">telefonisch unter</p>
  <div class="phone">
    <svg width="18" height="18" viewBox="0 0 18 18" aria-hidden="true"><circle cx="9" cy="9" r="9" fill="#f7b9da"/><path d="M6 4.5l1.6 2.4-1 1c.6 1.3 1.6 2.3 2.9 2.9l1-1 2.4 1.6-.8 1.6c-3.6-.3-6.6-3.3-6.9-6.9z" fill="#fff"/></svg>
    0664 291 846 37
  </div>
  <p class="phone-end">entgegenzunehmen.</p>
  <div class="cta">RUFEN SIE UNS AN UND SICHERN SIE SICH IHREN WUNSCHTERMIN!</div>

  <div class="cut-line"></div>
  <section class="voucher">
    <div class="voucher-gold"></div>
    <div class="v-title">Exklusiver</div>
    <div class="v-sub">ERÖFFNUNGSGUTSCHEIN</div>
    <p class="v-note">Zur Feier unserer Neueröffnung möchten wir Ihnen etwas Besonderes schenken</p>
    <div class="v-bow" role="img" aria-label="Goldene Geschenkschleife"></div>
    <div class="v-kicker">PROFITIEREN SIE VON</div>
    <div class="v-percent">30%</div>
    <div class="v-rabatt">RABATT</div>
    <div class="v-scope">AUF ALLE UNSERE<br>BEHANDLUNGEN</div>
    <div class="v-gift"><b>EIN GESCHENK</b><br>FÜR SIE UND<br>IHRE FÜẞE!</div>
    <p class="v-terms">*Dieser Gutschein ist gültig bis zum 31.12.2024 und einmalig einlösbar.<br>Bitte beachten Sie, dass er nicht mit anderen Aktionen kombinierbar ist.</p>
  </section>
</main>
</body>
</html>
```